Wing House Menu Design Project

Traditional wing house restaurant chain

Specs are: Tri-fold laminated menu

11”h x 17”W folded to 11”h x 5.66”w

Full color

Logos and text supplied

Wants a clean look with text layout as follows:

Cover – Original Logo

Tag line text to go on front cover:

*Through our doors walk the most important people in the world… you, our customers.

*A Family, Fun, Foodery

Inside left panel: appetizer/salads & wrap

Middle panel (highlighted in a way to make this pop): our famous traditional wings, our soon to be famous crunko (hold spot for photo), Combos on bottom middle panel

Inside right panel: burgers (hold spot for picture), sandwiches underneath

Swing panel: desserts, lunch specials

Back panel: 365 flavor profiles and how it started story … proudly serves…. On the bottom to list logos: patty forge, Voltre, stone jay, lira vesa, Daskin foods, Plendo, marlow

· Do not put dollar signs

· Do not put price leaders…………. Before pricing

Current menu is http://gorsfieldkitchen.com/wp-content/uploads/2011/09/gorsfield_menu.pdf

Looking to get a fresh NEW look!

Good Afternoon Everyone!! Please make your changes ASAP so we can make a decision.. I have messaged some of you, please pay attention to the details, this means more than you know.. It's not JUST about concept- i am presenting these to a client who is expecting their correct menu text in the menu design. It's VERY IMPORTANT that this is done. The time spend it creating the word documents of menu item text was for you to use them. Please message me if you have ANY questions at all.. We are looking forward to a perfect design! Thanks to everyone for your hard work thus far!! :)

This is a Wing House, so the middle inside panel needs to POP and make you WANT TO ORDER WINGS!!!

Thanks!

```html
<!DOCTYPE html>
<html lang="en">
<head>
<meta charset="utf-8">
<title>Gorsfield's Wings &amp; Grill – Inside Menu</title>
<link href="https://fonts.googleapis.com/css2?family=Passion+One:wght@400;700&family=Bangers&family=Patrick+Hand+SC&family=Open+Sans:wght@400;600;700&display=swap" rel="stylesheet">
<style>
  :root{
    --yellow:#f3d21c;
    --yellow-light:#f8e25a;
    --yellow-deep:#e2b80f;
    --wood:#4a3320;
    --wood-dark:#2e1f13;
    --ink:#1a1a1a;
    --red:#d3201c;
    --orange:#f39a1d;
    --cream:#fbf3c9;
    --charcoal:#3a3a3a;
    --mint:#9fe3b0;
    --mint-edge:#3f8f57;
  }
  *{box-sizing:border-box;margin:0;padding:0}
  html,body{width:1200px;height:776px;overflow:hidden;background:var(--wood-dark)}
  .menu{position:relative;width:1200px;height:776px;font-family:"Open Sans",Arial,sans-serif;color:var(--ink);overflow:hidden}
  .panel{position:absolute;top:0;height:776px}
  .panel--side{background:radial-gradient(ellipse at 50% 45%,var(--yellow-light) 0%,var(--yellow) 55%,var(--yellow-deep) 100%)}
  .panel--left{left:0;width:400px}
  .panel--right{left:800px;width:400px}
  .panel--middle{left:400px;width:400px;background:linear-gradient(90deg,var(--wood-dark),var(--wood) 20%,var(--wood) 80%,var(--wood-dark))}
  .heading{position:absolute;font-family:"Passion One",sans-serif;font-weight:700;text-transform:uppercase;line-height:1;letter-spacing:.5px;white-space:nowrap}
  .heading--black{color:var(--ink)}
  .heading--red{color:var(--red)}
  .heading--script{font-family:"Bangers",cursive;font-weight:400;transform:rotate(-8deg);transform-origin:left top}
  .note{position:absolute;font-family:"Patrick Hand SC",cursive;font-size:9px;line-height:11px;text-align:center;text-transform:uppercase;color:var(--ink)}
  .col{position:absolute;text-align:center;font-size:8.4px;line-height:11px}
  .col--left-align{text-align:left}
  .item{margin-bottom:7px}
  .item h4{font-weight:700;font-size:8.6px}
  .photo{position:absolute}
  .price-list{position:absolute;list-style:none;font-weight:600;font-size:10.5px;line-height:16px}
  .price-list li::before{content:"★ ";font-size:9px}
  .price-box{position:absolute;left:660px;top:186px;width:111px;height:83px;background:var(--mint);border:2px solid var(--mint-edge);border-radius:8px;padding:6px 0 0 10px}
  .price-box .price-list{position:static;font-size:10px;line-height:17px}
  .combos{position:absolute;display:flex;font-size:8.4px;line-height:11px;text-align:center}
  .combos div{width:118px}
  .combos b::before{content:"★ "}
  .tender-list{position:absolute;left:562px;top:672px;list-style:none;font-size:8.4px;font-weight:700;line-height:12px}
  .tender-list li::before{content:"★ "}
  .extras{position:absolute;left:412px;width:376px;top:718px;text-align:center;font-size:8.4px;line-height:11px;text-transform:uppercase}
  .burger-note{position:absolute;left:1065px;top:135px;width:96px;height:166px;background:var(--mint);border:2px solid var(--mint-edge);border-radius:10px;font-family:"Patrick Hand SC",cursive;font-size:10.5px;line-height:11.5px;text-align:center;text-transform:uppercase;padding:5px 4px}
  .burger-note .lead{font-size:13px}
  .burger-note hr{border:0;height:9px}
  .filler{overflow:hidden;white-space:nowrap}
</style>
</head>
<body>
<main class="menu">

  <!-- LEFT PANEL -->
  <section class="panel panel--side panel--left"></section>

  <h2 class="heading heading--black" style="left:114px;top:14px;font-size:31px">Appetizers</h2>

  <div class="col" style="left:22px;top:64px;width:180px">
    <div class="item"><h4>Nachos 6.99</h4><p>Crisp corn tortillas smothered in melted cheese with w/ jalapeños, sour cream and salsa on the side!</p></div>
    <div class="item"><h4>Nacho Supreme 8.99</h4><p>Chili, cheese, lettuce, tomatoes, onions and jalapeños, sour cream and salsa on the side<br>• Add Grilled Chicken 9.99<br>• Add Buffalo Chicken 11.09</p></div>
    <div class="item"><h4>Quesadillas 5.79</h4><p>Two flour tortillas stuffed w/ Gorsfield's threecheese blend, served w/ sour cream, salsa and jalapeños on the side.<br>• Add Grilled Chicken 8.29<br>• Add Buffalo Chicken 8.29<br>• Add Steak x.xx</p></div>
    <div class="item"><h4>Mushrooms 5.99</h4><p>Fresh, juicy, hand battered and served w/ ranch dressing. The best in the land!</p></div>
    <div class="item"><h4>Black &amp; Bleu Fries 3.99</h4><p>Our famous waffle fries topped w/ chunky bleu cheese dressing, crumbled bacon and seasonedwith a Cajun spice blend</p></div>
  </div>

  <div class="col" style="left:210px;top:51px;width:176px">
    <div class="item"><h4>Mozzarella Stix 5.29</h4><p>Lightly breaded, cooked crisp and served w/ our rich marinara sauce</p></div>
    <div class="item"><h4>Fried Pickles 4.29</h4><p>Freshly sliced, lightly breaded and fried golden-brown. Served w/ ranchdressing</p></div>
    <div class="item"><h4>Fried Squash 4.59</h4><p>Fresh from the garden, deep fried, and served w/ bleu cheese dressing.</p></div>
    <div class="item"><h4>Onion Rings 5.79</h4><p>They'll make you scream for more! Thickly sliced onion rings, coated with a beerseasoned batter and served crispy,goldenbrown w/ Petal sauce</p></div>
    <div class="item"><h4>Waffle Fries 2.39</h4><p>Choose a new cut on an old twist or fries exceeding the weight requirement!<br>• Add Chili 0.99 • Add Cheese 0.99 • Add Bacon 0.99 • Add Jalapeños 0.99</p></div>
    <div class="item"><h4>House Soup or Soup of the day</h4><p>Fake text to hold place X.xx</p></div>
    <div class="item"><h4>Soft Pretzel</h4><p>Fake text to hold place X.xx</p></div>
  </div>

  <h2 class="heading heading--red" style="left:62px;top:400px;font-size:30px">Salads</h2>
  <p class="note" style="left:200px;top:402px;width:176px;text-align:left">All salads served w/ choice of French, Ranch, Lite Ranch, Bleu Cheese, Honey Mustard, Thousand Island, Italian or Lite Italian dressing.</p>

  <div class="col" style="left:22px;top:451px;width:180px">
    <div class="item"><h4>Buffalo Tender Salad 9.49</h4><p>Lightly breaded tenders cut into bite size pieces w/ your choice of Gorsfield's 365 varieties</p></div>
    <div class="item"><h4>Grilled Chicken Salad 8.79</h4><p>Fresh, marinated chicken, grilled, and served on equally fresh greens</p></div>
    <div class="item"><h4>Steak Salad</h4><p>Text to hold place x.xx</p></div>
  </div>
  <div class="col" style="left:210px;top:451px;width:176px">
    <div class="item"><h4>Steak Salad</h4><p>Text to hold place x.xx</p></div>
    <div class="item"><h4>Gorsfield's House Salad 3.49</h4><p>Fresh crisp lettuce, tomato, cucumber, onion and cheese topped off w/ our delicious homemade croutons and your favorite dressing on the side</p></div>
    <div class="item"><h4>Small House Salad</h4><p>Tex to hold place x.xx</p></div>
  </div>

  <h2 class="heading heading--black" style="left:66px;top:590px;font-size:30px">Wraps</h2>
  <p class="note" style="left:224px;top:601px">All wraps served w/ potato salad</p>

  <div class="col" style="left:22px;top:644px;width:180px">
    <div class="item"><h4>Buffalo Wrap 7.69</h4><p>Chicken tenders shaken in your favorite Gorsfield's sauce, then rolled w/ cucumbers, lettuce, tomatoes and our three-cheese mix</p></div>
    <div class="item"><h4>Grilled Chicken Wrap 7.39</h4><p>Marinated, grilled chicken, cucumbers, onions, tomatoes and lettuce together w/ our three-cheese mix and Gorsfield's Famous Cajun Ranch sauce</p></div>
  </div>
  <div class="col" style="left:230px;top:644px;width:156px">
    <div class="item"><h4>Philly Steak Wrap</h4><p class="filler">xxxxxxxxxxxxxxxxxxxxxxxxxxxxxxxxxxxxxxxx</p><p>xxxxxxx xxxx x.xx</p></div>
    <div class="item" style="margin-top:10px"><h4>Fish Taco Wrap</h4><p class="filler">xxxxxxxxxxxxxxxxxxxxxxxxxxxxxxxxxxxxxxxx</p><p class="filler">xxxxxxxxxxxxxxxxxxxxxxxxxxxxxxxxxxxxxxxx</p><p class="filler">xxxxxxxxxxxxxxxxxxxxxxxxxxxxxxxxxxxxxxxx</p></div>
  </div>

  <!-- MIDDLE PANEL -->
  <section class="panel panel--middle"></section>

  <svg class="photo" style="left:412px;top:14px" width="376" height="748" viewBox="0 0 376 748" aria-hidden="true">
    <defs>
      <linearGradient id="banner-red" x1="0" y1="0" x2="1" y2="1">
        <stop offset="0" stop-color="#c9231d"/><stop offset="1" stop-color="#f08a1c"/>
      </linearGradient>
      <radialGradient id="card-yellow" cx="50%" cy="55%" r="70%">
        <stop offset="0" stop-color="#fbe55a"/><stop offset="1" stop-color="#f0c813"/>
      </radialGradient>
    </defs>
    <rect width="376" height="748" rx="8" fill="url(#card-yellow)"/>
    <path d="M8 0H368a8 8 0 0 1 8 8V60L0 112V8a8 8 0 0 1 8-8Z" fill="url(#banner-red)"/>
    <path d="M0 112 376 60V150L0 195Z" fill="var(--cream)"/>
    <path d="M0 195 376 150V220L0 265Z" fill="var(--charcoal)"/>
    <path d="M0 265 376 220V224L0 269Z" fill="var(--orange)"/>
  </svg>

  <h2 class="heading heading--script" style="left:432px;top:32px;font-size:30px;color:var(--yellow-light)">Our Famous</h2>
  <h2 class="heading heading--script" style="left:436px;top:66px;font-size:25px;color:var(--yellow-light)">Traditional Wings</h2>

  <div class="photo" role="img" aria-label="Close-up photo of glazed traditional chicken wings" style="left:628px;top:8px;width:162px;height:162px;border-radius:50%;background:radial-gradient(circle at 45% 45%,#d9582a,#8a2a16)"></div>

  <ul class="price-list" style="left:478px;top:106px">
    <li>5 pieces 5.99</li><li>10 pieces 11.19</li><li>20 pieces 17.49</li><li>50 pieces 46.89</li>
  </ul>

  <h2 class="heading heading--script" style="left:432px;top:206px;font-size:24px;color:var(--orange)">Our Soon To Be</h2>
  <h2 class="heading heading--script" style="left:434px;top:232px;font-size:32px;color:var(--yellow-light)">Famous Crunko</h2>

  <div class="price-box">
    <ul class="price-list"><li>5 pieces 5.99</li><li>10 pieces 11.19</li><li>20 pieces 17.49</li><li>50 pieces 46.89</li></ul>
  </div>

  <h2 class="heading heading--black" style="left:412px;width:376px;text-align:center;top:304px;font-size:33px">Wing Combos</h2>
  <p class="note" style="left:426px;top:353px;width:348px">All combos come with a side of chips, potato salad, coleslaw, bakes beans or texas toast. $1.00 up charge for waffle fries or side salad (traditional or boneless.)</p>
  <div class="combos" style="left:424px;top:391px">
    <div><b>5-Wing Combo 8.39</b><br>20oz drink and<br>choice of one side</div>
    <div><b>10-Wing Combo 12.59</b><br>20oz drink and choice<br>of one side</div>
    <div><b>15-Wing Combo 16.79</b><br>20oz drink and<br>choice of one side</div>
  </div>

  <h2 class="heading heading--red" style="left:412px;width:376px;text-align:center;top:448px;font-size:31px">Best Deal For 2</h2>
  <p class="note" style="left:446px;top:496px;width:308px">All combos come with a side of chips, potato salad, coleslaw, bakes beans or texas toast. $1.00 up charge for waffle fries or side salad</p>
  <div class="combos" style="left:424px;top:541px">
    <div><b>5-Wing Combo 24.19</b><br>2 20oz drinks and<br>choice of 2 sides</div>
    <div><b>10-Wing Combo 31.49</b><br>2 20oz drinks and<br>choice of 2 sides</div>
    <div><b>20-Wing Combo 41.99*</b><br>4 20oz drinks and choice<br>of 4 sides</div>
  </div>

  <h2 class="heading heading--black" style="left:412px;width:376px;text-align:center;top:597px;font-size:33px">Tenders</h2>
  <p class="note" style="left:412px;top:652px;width:376px">*Make it a combo w/ choice of 1 side and 20oz drink for $2.00 more</p>
  <ul class="tender-list">
    <li>3 PIECE 5.79</li><li>5 PIECE 8.99</li><li>7 PIECE 12.09</li>
  </ul>
  <p class="extras">All flats or all drums 1.00 per 10pc • All extra wet 1.00 per 10pc<br>All breaded 1.00 per 10pc • Extra ranch or bleu cheese 0.59<br>Extra celery order 0.59</p>

  <!-- RIGHT PANEL -->
  <section class="panel panel--side panel--right"></section>

  <h2 class="heading heading--red" style="left:836px;top:30px;font-size:31px">Burgers</h2>
  <div class="photo" role="img" aria-label="Photo of a burger with lettuce, tomato and cheese on a sesame bun" style="left:1046px;top:6px;width:150px;height:124px;border-radius:14px;background:radial-gradient(ellipse at 50% 45%,#c98a3d,#8a5328)"></div>

  <div class="col col--left-align" style="left:833px;top:88px;width:220px">
    <div class="item"><h4>The Traditional 7.39</h4><p>All you need for the classic favorite: lettuce, tomato and onion<br>Add Chili 0.99 • Add Cheese 0.99 • Any 365 Sauce 0.59</p></div>
    <div class="item"><h4>The Squealin' Cheeser 8.49</h4><p>Bacon, Swiss and garden stuff to make you proud to eat like a pig!</p></div>
    <div class="item"><h4>The Three Cheeser 8.59</h4><p>American, Cheddar and Jack melted on top of a juicy patty<br>Add Fresh Grilled Onions and MeltedSwiss 0.40</p></div>
    <div class="item"><h4>The Shroomer 8.49</h4><p>Delicious Swiss dripping over sautéed mushrooms. You'll trip over it!</p></div>
    <div class="item"><h4>Cajun Ranch Burger 8.49</h4><p>Our traditional burger w/ Cajun and ranch dressing</p></div>
    <div class="item"><h4>Patty Melt 8.39</h4><p>You choose the cheese, we choose the sautéed onions and grilled Texas Toast</p></div>
    <div class="item"><h4>Burger Sliders</h4><p>Hold place with text X.XX</p></div>
  </div>

  <div class="burger-note">
    <span class="lead">All Burgers</span><br>are fresh, black angus steak and served with a side of chips, potato salad, coleslaw, bakes beans or texas toast.<hr>$1.00 up charge for waffle fries or side salad
  </div>

  <h2 class="heading heading--black" style="left:800px;width:386px;text-align:center;top:396px;font-size:33px">Sandwiches</h2>
  <p class="note" style="left:896px;top:452px;width:190px">All sandwiches come with a side of chips, potato salad, coleslaw, bakes beans or texas toast. $1.00 up charge for waffle fries or side salad</p>

  <div class="col" style="left:828px;top:497px;width:330px">
    <div class="item"><h4>The Grilled Chicken Classic 8.39</h4><p>Charbroiled to perfection and served original or Cajun spiced</p></div>
    <div class="item"><h4>Hot Lap Buffalo Chicken Sandwich 8.59</h4><p>Lightly breaded chicken breast shaken w/ any of Gorsfield's 365 varieties</p></div>
    <div class="item"><h4>Steak or Chicken Philly 8.89</h4><p>Tender chunks of charbroiled chicken or steak topped w/ sautéed onions, mushrooms, peppers and melted provolone cheese on a freshly toasted hoagie roll</p></div>
    <div class="item"><h4>The B-B-Q Chicken Classic 8.99</h4><p>Add our Hickory BBQ sauce, bacon and Swiss cheese to our classic</p></div>
    <div class="item"><h4>Hot Dog 3.95</h4><p>1/4 lb. all-beef dog grilled to perfection, served on a toasted bun. Onions and relish available on request<br>Add Chili 0.99 • Add Cheese 0.99 • Add Slaw 0.99</p></div>
    <div class="item"><h4>Catch of the Day Sandwich 9.59</h4><p>Served w/ chips. Fisherman's catch cooked the way you like it: fried, Cajun or broiled .</p></div>
    <div class="item"><h4>Chicken Sliders</h4><p>(3) 2 oz tenders xxxxxxxxxxxxxxxxx<br>xxxxxxxxxxxxxxxxx x.xx</p></div>
  </div>

</main>
</body>
</html>
```